Business Cards and email stationery for VoiceOver Artist
Cutting Edge Business cards and email stationery for VoiceOver Artist
Use standard fonts
Not sure here?
Bright & Fun-filled
Marcus Dellow
Voiceover
2817 Palmera Ave
Encino CA 91427
(•••NO ADDRESS ON BUSINESS CARDS PLEASE••••)
818-555-2193 Cell
marcus@marcusdellow.example
marcusdellow.example
As 3-D as possible, cutting-edge, creative
1 Should be easy to read
2 Cell number should be listed first!
Uploaded Logo for VoiceOver Artist for Business cards and email Stationery
Logo for VoiceOver Artist v2

```html
<!DOCTYPE html>
<html lang="en">
<head>
<meta charset="utf-8">
<title>Marcus Dellow Voiceover – Business Cards</title>
<link rel="stylesheet" href="https://fonts.googleapis.com/css2?family=Oswald:wght@400;600&family=Roboto:wght@400;500&display=swap">
<style>
  :root {
    --bg: #e9e9ea;
    --red-light: #e8353b;
    --red: #c8161d;
    --red-dark: #7d0a0f;
    --grey: #4a4a4c;
    --grey-dark: #333335;
    --silver: #e6e6e6;
    --silver-dark: #9a9a9a;
    --text-light: #f2f2f2;
  }
  * { margin: 0; padding: 0; box-sizing: border-box; }
  html, body { width: 1200px; height: 864px; overflow: hidden; background: var(--bg); }
  .canvas {
    width: 1200px; height: 864px;
    display: flex; flex-direction: column; align-items: center; justify-content: center; gap: 24px;
  }
  .card {
    position: relative; width: 700px; height: 400px; border-radius: 22px; overflow: hidden;
    box-shadow: 0 10px 24px rgba(0,0,0,.25);
  }
  /* Front */
  .card-front {
    background: radial-gradient(ellipse at 50% 40%, var(--red-light) 0%, var(--red) 45%, var(--red-dark) 100%);
  }
  .front-mark {
    position: absolute; left: 0; right: 0; top: 130px;
    display: flex; align-items: center; justify-content: center; gap: 18px;
  }
  .mark-circle {
    width: 70px; height: 70px; border-radius: 50%;
    background: linear-gradient(160deg, var(--silver) 0%, var(--silver-dark) 100%);
  }
  .mark-name {
    font-family: "Oswald", sans-serif; font-weight: 600; font-size: 40px; letter-spacing: 2px;
    color: var(--silver);
  }
  .front-url {
    position: absolute; left: 0; right: 0; bottom: 48px; text-align: center;
    font-family: "Roboto", sans-serif; font-size: 14px; letter-spacing: 5px; color: var(--text-light);
  }
  /* Back */
  .card-back { background: linear-gradient(180deg, var(--grey) 0%, var(--grey-dark) 100%); }
  .back-shape { position: absolute; inset: 0; }
  .back-mark {
    position: absolute; left: 34px; top: 40px; width: 54px; height: 54px; border-radius: 50%;
    background: linear-gradient(160deg, var(--silver) 0%, var(--silver-dark) 100%);
  }
  .back-name {
    position: absolute; left: 110px; top: 22px;
    font-family: "Oswald", sans-serif; font-weight: 600; font-size: 62px; letter-spacing: 1px;
    color: var(--text-light); line-height: 1;
  }
  .back-role {
    position: absolute; left: 170px; top: 112px;
    font-family: "Oswald", sans-serif; font-weight: 400; font-size: 22px; letter-spacing: 14px;
    color: var(--red);
  }
  .contact-list {
    position: absolute; right: 36px; top: 210px; list-style: none;
    font-family: "Roboto", sans-serif; font-size: 15px; color: var(--text-light);
  }
  .contact-list li { display: flex; align-items: center; gap: 10px; margin-bottom: 10px; }
  .contact-icon { width: 20px; height: 20px; }
  .back-signature {
    position: absolute; left: 40px; bottom: 36px;
    font-family: "Roboto", sans-serif; color: var(--text-light);
  }
  .signature-name { font-size: 18px; font-weight: 500; letter-spacing: 2px; }
  .signature-role { font-size: 13px; letter-spacing: 4px; margin-top: 4px; color: #bdbdbd; }
</style>
</head>
<body>
<main class="canvas">
  <section class="card card-front">
    <div class="front-mark">
      <span class="mark-circle"></span>
      <span class="mark-name">MARCUSDELLOW</span>
    </div>
    <p class="front-url">WWW.MARCUSDELLOW.EXAMPLE</p>
  </section>

  <section class="card card-back">
    <svg class="back-shape" viewBox="0 0 700 400" aria-hidden="true">
      <defs>
        <radialGradient id="backRed" cx="40%" cy="30%" r="80%">
          <stop offset="0" stop-color="#e8353b"/>
          <stop offset=".5" stop-color="#c8161d"/>
          <stop offset="1" stop-color="#7d0a0f"/>
        </radialGradient>
        <linearGradient id="silverBand" x1="0" x2="1">
          <stop offset="0" stop-color="#f4f4f4"/>
          <stop offset=".6" stop-color="#cfcfcf"/>
          <stop offset="1" stop-color="#8a8a8a"/>
        </linearGradient>
      </defs>
      <path d="M0 0 H700 V110 C560 150 380 200 0 230 Z" fill="url(#backRed)"/>
      <path d="M150 104 H660 L640 144 C520 160 400 172 150 180 Z" fill="url(#silverBand)" opacity=".95"/>
      <path d="M0 230 C380 200 560 150 700 110 V122 C560 164 380 214 0 244 Z" fill="#d9d9d9"/>
    </svg>
    <span class="back-mark"></span>
    <h1 class="back-name">MARCUSDELLOW</h1>
    <p class="back-role">VOICEOVER</p>
    <ul class="contact-list">
      <li>
        <svg class="contact-icon" viewBox="0 0 20 20" aria-hidden="true"><circle cx="10" cy="10" r="10" fill="#c8161d"/><path d="M7 5h2l1 3-1.5 1a6 6 0 0 0 2.5 2.5L12 10l3 1v2a1 1 0 0 1-1 1A9 9 0 0 1 6 6a1 1 0 0 1 1-1z" fill="#fff"/></svg>
        818-555-2193 Cell
      </li>
      <li>
        <svg class="contact-icon" viewBox="0 0 20 20" aria-hidden="true"><circle cx="10" cy="10" r="10" fill="#c8161d"/><rect x="5" y="6.5" width="10" height="7" fill="none" stroke="#fff" stroke-width="1.3"/><path d="M5 6.5l5 4 5-4" fill="none" stroke="#fff" stroke-width="1.3"/></svg>
        marcus@marcusdellow.example
      </li>
      <li>
        <svg class="contact-icon" viewBox="0 0 20 20" aria-hidden="true"><circle cx="10" cy="10" r="10" fill="#c8161d"/><circle cx="10" cy="10" r="5" fill="none" stroke="#fff" stroke-width="1.2"/><path d="M5 10h10M10 5c-2.5 3-2.5 7 0 10M10 5c2.5 3 2.5 7 0 10" fill="none" stroke="#fff" stroke-width="1"/></svg>
        www.marcusdellow.example
      </li>
    </ul>
    <div class="back-signature">
      <p class="signature-name">MARCUS DELLOW</p>
      <p class="signature-role">VOICEOVER</p>
    </div>
  </section>
</main>
</body>
</html>
```